Website re-design for a Gardening - Vegetable Growing -Compost Ecommerce site

We need a "green & organic" looking web design for The Loam Barrow website re-design. The website sells garden and landscape supplies, and specialises in composites and vegetable growing products which are sold nationwide throughout the UK.

This project is for a homepage & content page design which can be used as a template to create other pages through the site, ideally with css and coding for a joomla template.

Our customer base is made up of gardeners & vegetable growers. The site is an ecommerce site run on Joomla CMS, we will be converting the design into a joomla template.

The Home page will contain information and attractive garden & vegetable growing images linking to information and product / shop category pages.

Current site: www.theloambarrow.co.uk

Sites I like the look of :

http://fernquillplot.com/index.php
http://albumpage.stationnine.com
http://www.squirmydelvers.co.uk/
http://www.hamletcreamery.co.uk
Updates

Hi Guys! Feel free to use different colour schemes from the three colours i have suggested in the brief. I am open to any suggestions, but a modern look and feel is preferred.

Target Market(s)

Home owners, vegetable growers and keen gardeners

Industry/Entity Type

Landscape

Coding

Coded - Design and coding required

Font styles to use
Sans Serif

Colors
9bcb3c
faa54b
fece3e

Requirements
Must have
• a white main content background

```html
<!DOCTYPE html>
<html lang="en">
<head>
<meta charset="utf-8">
<title>The Loam Barrow – Compost &amp; Garden Supplies</title>
<link rel="stylesheet" href="https://fonts.googleapis.com/css2?family=Questrial&family=Oswald:wght@300;500;700&family=Montserrat:wght@600;700&family=Open+Sans:wght@400;700&family=Roboto:wght@400&display=swap">
<style>
:root{
  --green:#8cc63f;
  --green-dark:#46a538;
  --orange:#f7a53b;
  --yellow:#fed33e;
  --purple:#7b5a82;
  --teal:#5cc3a0;
  --grey:#555;
  --grey-light:#999;
  --line:#e2e2e2;
  --red:#d9352a;
  --white:#fff;
}
*{margin:0;padding:0;box-sizing:border-box}
html,body{width:891px;height:1200px;overflow:hidden;background:var(--white)}
body{position:relative;font-family:"Questrial",sans-serif;color:var(--grey)}

/* header */
.site-header{position:absolute;left:0;top:0;width:891px;height:150px;background:linear-gradient(#d9ecfa 0%,#fff 70%)}
.brand{position:absolute;display:flex;align-items:center;gap:8px;color:var(--green);font-family:"Questrial",sans-serif;white-space:nowrap}
.brand-dot{width:30px;height:30px;border-radius:50%;background:var(--yellow)}
.brand-name{font-size:26px;line-height:1}
.header-brand{left:125px;top:34px}
.account-links{position:absolute;left:560px;top:25px;font-size:9.5px;color:var(--grey);display:flex;gap:6px;align-items:center;font-family:"Roboto",sans-serif}
.account-links .cart{display:flex;align-items:center;gap:6px;margin-right:14px}
.phone{position:absolute;left:656px;top:47px;font-family:"Roboto",sans-serif;font-size:14px;color:#333;display:flex;align-items:center;gap:6px}
.main-nav{position:absolute;left:125px;top:109px;width:656px;display:flex;justify-content:space-between;font-size:10.5px;letter-spacing:.3px;color:var(--grey)}
.main-nav a{color:inherit;text-decoration:none}
.main-nav .sep{width:1px;height:26px;background:var(--line);margin-top:-7px}

/* hero */
.hero{position:absolute;left:0;top:150px;width:891px;height:287px;background:linear-gradient(100deg,#b6c9a0 0%,#7e9c5a 22%,#496b2b 45%,#6d8e37 70%,#8aa94a 100%)}
.hero-kicker{position:absolute;left:450px;top:61px;font-family:"Oswald",sans-serif;font-weight:300;font-size:17px;color:#c8e27a}
.hero-title{position:absolute;left:450px;top:84px;font-family:"Oswald",sans-serif;font-weight:700;font-size:36px;line-height:39px;letter-spacing:-.5px;text-transform:uppercase}
.hero-title .y{color:var(--yellow)}.hero-title .o{color:var(--orange)}.hero-title .g{color:#9bcb3c}
.hero-tail{position:absolute;left:654px;top:165px;font-family:"Oswald",sans-serif;font-weight:300;font-size:27px;color:#d8ec9a}
.hero-arrows{position:absolute;left:735px;top:63px;display:flex;gap:2px}
.hero-arrows span{width:19px;height:19px;background:rgba(140,198,63,.75);display:flex;align-items:center;justify-content:center}
.hero-dots{position:absolute;left:733px;top:236px;display:flex;gap:4px}
.hero-dots i{width:7px;height:7px;border-radius:50%;background:#fff}
.hero-dots i.on{background:var(--green)}

/* promo band */
.promo{position:absolute;left:0;top:437px;width:891px;height:110px;background:var(--purple);text-align:center;font-family:"Montserrat",sans-serif}
.promo-line1{position:absolute;left:0;width:100%;top:17px;color:#fff;font-size:14.5px;font-weight:600}
.promo-line2{position:absolute;left:0;width:100%;top:37px;color:var(--yellow);font-size:18px;font-weight:700}
.btn{display:inline-flex;align-items:center;justify-content:center;background:var(--green);color:#fff;border-radius:16px;font-family:"Open Sans",sans-serif;font-weight:700;text-transform:uppercase}
.promo .btn{position:absolute;left:397px;top:68px;width:103px;height:29px;font-size:11.5px}

/* featured */
.section-title{position:absolute;font-family:"Questrial",sans-serif;font-weight:400;font-size:21px;color:var(--grey);text-transform:uppercase;white-space:nowrap}
.section-title .hl{color:var(--green)}
.view-all{position:absolute;left:458px;top:582px;width:117px;height:26px;border:1px solid #ccc;font-size:8.5px;color:var(--grey-light);display:flex;align-items:center;justify-content:center;gap:5px}
.carousel{position:absolute;left:125px;top:623px;width:467px;height:188px;background:var(--green)}
.carousel-arrow{position:absolute;top:80px}
.products{position:absolute;left:16px;top:0;width:435px;height:188px;background:#fff;display:flex;gap:4px;padding:1px 0}
.product{flex:1;border:1px solid var(--line);position:relative;box-shadow:inset 0 0 0 2px #f5f5f5}
.product h3{position:absolute;left:13px;top:10px;font-weight:400;font-size:11px;line-height:12px;color:#444}
.product .thumb{position:absolute;left:42px;top:43px;width:60px;height:90px}
.product .btn{position:absolute;left:32px;top:165px;width:73px;height:18px;font-size:8.5px;border-radius:9px}

.bubble{position:absolute;left:600px;top:574px;width:162px;height:124px}
.bubble-text{position:absolute;left:628px;top:598px;width:108px;text-align:center;color:#fff;font-family:"Open Sans",sans-serif;font-weight:700;font-size:11px;line-height:14px}
.quote{position:absolute;color:#fff;font-family:"Open Sans",sans-serif;font-weight:700;font-size:22px;line-height:1}
.benefits{position:absolute;left:624px;top:714px;list-style:none;font-size:12px;color:#444;line-height:17.4px}
.benefits li{display:flex;align-items:center;gap:5px}
.order-btn{position:absolute;left:638px;top:792px;width:86px;height:18px;font-size:8.5px}

/* welcome */
.welcome-copy{position:absolute;left:138px;top:922px;width:408px;font-family:"Open Sans",sans-serif;font-size:9px;line-height:13.3px;color:#333}
.welcome-copy p+p{margin-top:13px}
.readmore{position:absolute;left:137px;top:1018px;width:81px;height:24px;font-size:8.5px;background:var(--green-dark)}
.yard-photo{position:absolute;left:574px;top:878px;width:196px;height:128px;background:linear-gradient(#b8c4c8 0%,#93a29a 40%,#4a3a2c 62%,#3a2c20 100%)}

/* footer */
.footer{position:absolute;left:0;top:1084px;width:891px;height:70px;border-top:1px solid var(--line);border-bottom:1px solid var(--line)}
.footer-brand{left:139px;top:1109px;gap:6px}
.footer-brand .brand-dot{width:24px;height:24px}
.footer-brand .brand-name{font-size:19px}
.newsletter{position:absolute;left:334px;top:1105px;width:201px;height:29px;border:1px solid var(--green);font-size:8.5px;color:#777;display:flex;align-items:center;justify-content:space-between;padding:0 10px}
.send{position:absolute;left:539px;top:1105px;width:80px;height:29px;background:var(--green-dark);color:#fff;font-family:"Open Sans",sans-serif;font-size:8.5px;display:flex;align-items:center;justify-content:center}
.barrow{position:absolute;left:631px;top:1043px;width:172px;height:110px;background:radial-gradient(ellipse at 50% 60%,#c9c9c9 0%,#e8e8e8 45%,rgba(255,255,255,0) 72%)}
.copyright{position:absolute;left:0;width:891px;top:1166px;text-align:center;font-family:"Open Sans",sans-serif;font-size:10px;color:var(--green-dark)}
</style>
</head>
<body>

<header class="site-header">
  <div class="brand header-brand"><span class="brand-dot"></span><span class="brand-name">The Loam Barrow</span></div>
  <div class="account-links">
    <span class="cart"><svg width="12" height="11" viewBox="0 0 12 11"><path d="M0 1h2l2 6h6l2-5H3" fill="none" stroke="#46a538" stroke-width="1.5"/><circle cx="5" cy="9.5" r="1" fill="#46a538"/><circle cx="9" cy="9.5" r="1" fill="#46a538"/></svg>0 - item</span>
    <span>My Account</span>|<span>My Wishlist</span>|<span>Checkout</span>
  </div>
  <div class="phone"><svg width="14" height="14" viewBox="0 0 14 14"><circle cx="7" cy="7" r="7" fill="#46a538"/><path d="M4.5 3.8l1.3-.3.8 1.8-.9.7c.4.9 1.1 1.6 2 2l.7-.9 1.8.8-.3 1.3c-3 .2-5.6-2.4-5.4-5.4z" fill="#fff"/></svg>(818) 555 01234</div>
  <nav class="main-nav">
    <a>HOME</a><span class="sep"></span><a>PRODUCTS</a><span class="sep"></span><a>ABOUT US</a><span class="sep"></span><a>WHAT WE DO</a><span class="sep"></span><a>GARDEN GURU</a><span class="sep"></span><a>BLOG</a><span class="sep"></span><a>BULK LOADS</a><span class="sep"></span><a>CONTACT US</a>
  </nav>
</header>

<section class="hero" role="img" aria-label="Photo of a gardener holding a crate of freshly harvested vegetables in a green garden">
  <div class="hero-kicker">Huge Range From</div>
  <div class="hero-title"><span class="y">Multi Purpose</span> <span class="o">To</span><br><span class="o">Specialist</span> <span class="g">Compost</span></div>
  <div class="hero-tail">Products !</div>
  <div class="hero-arrows">
    <span><svg width="7" height="10"><path d="M6 1L2 5l4 4" fill="none" stroke="#fff" stroke-width="1.2"/></svg></span>
    <span><svg width="7" height="10"><path d="M1 1l4 4-4 4" fill="none" stroke="#fff" stroke-width="1.2"/></svg></span>
  </div>
  <div class="hero-dots"><i></i><i class="on"></i><i></i><i></i></div>
</section>

<section class="promo">
  <p class="promo-line1">We Supply a huge Range of compost products including organic composts,</p>
  <p class="promo-line2">peat free compost, ericaceous composts etc all at unbeatable prices!</p>
  <a class="btn">Visit Store</a>
</section>

<h2 class="section-title" style="left:125px;top:583px"><span class="hl">Featured</span> Products</h2>
<div class="view-all"><svg width="10" height="10"><circle cx="4" cy="4" r="3" fill="none" stroke="#999"/><path d="M6.3 6.3L9 9" stroke="#999"/></svg>VIEW ALL PRODUCTS</div>

<div class="carousel">
  <svg class="carousel-arrow" style="left:3px" width="10" height="28"><path d="M8 1L2 14l6 13" fill="none" stroke="#fff"/></svg>
  <div class="products">
    <div class="product"><h3>Organic Compost<br>Bulk Bag</h3><div class="thumb" role="img" aria-label="Multipurpose compost bag" style="background:linear-gradient(#e9e4ef,#7a2a7c)"></div><a class="btn">Buy Now</a></div>
    <div class="product"><h3>Children's Veg<br>Garden</h3><div class="thumb" role="img" aria-label="Seedling growing from a mound of soil" style="background:radial-gradient(ellipse at 50% 80%,#5a3f2a 0%,#7a5a3e 45%,#fff 72%)"></div><a class="btn">Buy Now</a></div>
    <div class="product"><h3>Mushroom Compost</h3><div class="thumb" role="img" aria-label="Mushroom compost bag" style="background:linear-gradient(#4fa53c,#2f7a2a)"></div><a class="btn">Buy Now</a></div>
  </div>
  <svg class="carousel-arrow" style="left:455px" width="10" height="28"><path d="M2 1l6 13-6 13" fill="none" stroke="#fff"/></svg>
</div>

<svg class="bubble" viewBox="0 0 162 124" aria-hidden="true">
  <g fill="#5cc3a0">
    <rect x="10" y="14" width="142" height="86" rx="36"/>
    <circle cx="42" cy="28" r="24"/><circle cx="82" cy="22" r="22"/><circle cx="122" cy="30" r="24"/>
    <circle cx="24" cy="62" r="22"/><circle cx="140" cy="62" r="20"/>
    <circle cx="50" cy="92" r="20"/><circle cx="112" cy="92" r="20"/>
    <path d="M58 100h24l-20 22z"/>
  </g>
</svg>
<span class="quote" style="left:616px;top:592px">“</span>
<span class="quote" style="left:728px;top:652px">”</span>
<p class="bubble-text">Order online before 1.00pm for next day delivery or book a delivery date!</p>

<ul class="benefits">
  <li><svg width="13" height="13"><rect x=".5" y="2.5" width="10" height="10" fill="none" stroke="#d9352a"/><path d="M3 7l2.5 3L12 1" fill="none" stroke="#d9352a" stroke-width="2"/></svg>Great Value</li>
  <li><svg width="13" height="13"><rect x=".5" y="2.5" width="10" height="10" fill="none" stroke="#d9352a"/><path d="M3 7l2.5 3L12 1" fill="none" stroke="#d9352a" stroke-width="2"/></svg>Quality Service</li>
  <li><svg width="13" height="13"><rect x=".5" y="2.5" width="10" height="10" fill="none" stroke="#d9352a"/><path d="M3 7l2.5 3L12 1" fill="none" stroke="#d9352a" stroke-width="2"/></svg>Fast Delivery</li>
  <li><svg width="13" height="13"><rect x=".5" y="2.5" width="10" height="10" fill="none" stroke="#d9352a"/><path d="M3 7l2.5 3L12 1" fill="none" stroke="#d9352a" stroke-width="2"/></svg>The Finest Products</li>
</ul>
<a class="btn order-btn">Order Online</a>

<h2 class="section-title" style="left:138px;top:878px">Welcome to <span class="hl">The Loam Barrow</span></h2>
<div class="welcome-copy">
  <p>We've got all the compost, topsoil and garden supplies you'll need to get your garden in shape this year! Whether you just need some compost to top up your flower beds or want to start growing your own fruit and veg, we have everything you'll need and much more!</p>
  <p>As the UK's leading supplier, we have an extensive range of growing media as well as many other garden products such as organic compost, vegetable growing kits and baby vegetable seedlings!</p>
</div>
<a class="btn readmore">Readmore</a>
<div class="yard-photo" role="img" aria-label="Photo of a large compost heap at the supply yard"></div>

<footer class="footer"></footer>
<div class="brand footer-brand"><span class="brand-dot"></span><span class="brand-name">The Loam Barrow</span></div>
<div class="newsletter"><span>SIGN UP FOR NEWSLETTER</span><svg width="14" height="10"><rect x=".5" y=".5" width="13" height="9" fill="none" stroke="#7b5a82"/><path d="M.5 .5l6.5 5 6.5-5" fill="none" stroke="#7b5a82"/></svg></div>
<div class="send">SEND</div>
<div class="barrow" role="img" aria-label="Illustration of a wheelbarrow with a shovel"></div>
<p class="copyright">Copyright © 2014 - All rights reserved.</p>

</body>
</html>
```